New business card for KT4 Linkway, a marketing company.

We need a new business card design. We would like it to be blue gray and white. We would like some movement but in a more subtle pattern than in the file we uploaded. We are a marketing company that connects brands with their target audiences - we make connections. We work in the New York Metro area with sophisticated clients. The card should feel modern, upscale and professional.

Target Market(s)

Businesses looking to grow their brands in tourism and nightlife. We work with liquor and beer companies and with Tourism bureaus and companies.

Industry/Entity Type

Marketing

Contact Information for Business Card

Would like a horizontal layout, two-sided. Would like the logo on the back with the tagline ' "connecting brands to their target audiences" under the logo. On the front, we would like name, title, contact email, contact phone, website.

Font styles to use
Sans Serif

Colors
3377b5
85cae6
ffffff

Requirements
Must have
• Our logo. See attached. Otherwise, open to your ideas.
Should not have
• No colors we don't want - no reds/pinks/oranges please

```html
<!DOCTYPE html>
<html lang="en">
<head>
<meta charset="utf-8">
<title>KT4 Linkway – Business Card</title>
<link rel="stylesheet" href="https://fonts.googleapis.com/css2?family=Lato:wght@300;400&family=Montserrat:wght@400;600&display=swap">
<style>
  :root {
    --brand-blue: #2b74b6;
    --accent-gray: #9a9a9a;
    --card-white: #ffffff;
    --text-gray: #555555;
    --text-dark: #444444;
    --rule-gray: #777777;
    --backdrop: #e9ebef;
  }
  * { margin: 0; padding: 0; box-sizing: border-box; }
  html, body { width: 1200px; height: 1200px; overflow: hidden; background: var(--backdrop); }
  .sheet {
    width: 1200px; height: 1200px;
    display: flex; flex-direction: column; align-items: center; justify-content: center; gap: 80px;
  }
  .card {
    position: relative; width: 700px; height: 400px;
    background: var(--card-white); border-radius: 36px; overflow: hidden;
    box-shadow: 0 12px 30px rgba(0,0,0,0.15);
    font-family: "Lato", sans-serif; color: var(--text-gray);
  }
  .card-art { position: absolute; inset: 0; width: 100%; height: 100%; }
  .brand-dot { display: block; border-radius: 50%; flex: none; }
  .brand-name {
    font-family: "Montserrat", sans-serif; font-weight: 400;
    letter-spacing: 1px; text-transform: uppercase; white-space: nowrap;
  }

  /* Back side */
  .card-back .brand { position: absolute; left: 220px; top: 118px; display: flex; align-items: center; gap: 14px; }
  .card-back .brand-dot { width: 84px; height: 84px; background: var(--brand-blue); }
  .card-back .brand-name { font-size: 32px; color: var(--brand-blue); }
  .back-info { position: absolute; right: 50px; top: 232px; text-align: right; }
  .back-web { font-size: 24px; letter-spacing: 1px; }
  .back-tagline { font-size: 14px; margin-top: 4px; letter-spacing: 0.4px; }

  /* Front side */
  .card-front .brand-dot { position: absolute; left: 560px; top: 30px; width: 90px; height: 90px; background: var(--card-white); }
  .card-front .brand-name {
    position: absolute; left: 628px; top: 128px;
    writing-mode: vertical-rl; font-size: 24px; color: var(--card-white);
  }
  .front-info { position: absolute; left: 60px; top: 70px; width: 400px; }
  .person-name { font-family: "Montserrat", sans-serif; font-size: 34px; font-weight: 400; color: var(--text-dark); }
  .person-title { font-size: 18px; margin-top: 2px; letter-spacing: 1px; }
  .rule { height: 1.5px; background: var(--rule-gray); margin: 18px 0; }
  .contact-line { display: flex; align-items: center; gap: 14px; font-size: 26px; line-height: 1.35; color: var(--text-dark); }
  .contact-line svg { width: 20px; height: 20px; fill: var(--text-dark); flex: none; }
  .front-web { font-size: 26px; letter-spacing: 1px; text-align: center; margin-top: 6px; color: var(--text-dark); }
</style>
</head>
<body>
<main class="sheet">

  <section class="card card-back" aria-label="Card back">
    <svg class="card-art" viewBox="0 0 700 400" preserveAspectRatio="none" aria-hidden="true">
      <path d="M520,0 C590,0 620,70 650,130 C670,170 690,190 700,195 L700,0 Z" fill="var(--accent-gray)"/>
      <path d="M555,0 C610,15 635,90 662,145 C678,178 692,195 700,200" fill="none" stroke="var(--accent-gray)" stroke-width="3"/>
      <path d="M0,400 L0,140 C60,130 110,140 140,190 C180,250 300,270 350,320 C375,345 380,380 380,400 Z" fill="var(--brand-blue)"/>
      <path d="M140,130 C170,190 200,225 260,250 C330,280 360,330 365,400" fill="none" stroke="var(--brand-blue)" stroke-width="3" transform="translate(-12,0)"/>
    </svg>
    <div class="brand">
      <span class="brand-dot"></span>
      <span class="brand-name">KT4 Linkway</span>
    </div>
    <div class="back-info">
      <p class="back-web">www.website.com</p>
      <p class="back-tagline">connecting brands to their target audiences</p>
    </div>
  </section>

  <section class="card card-front" aria-label="Card front">
    <svg class="card-art" viewBox="0 0 700 400" preserveAspectRatio="none" aria-hidden="true">
      <path d="M430,0 C540,50 600,200 610,400 L700,400 L700,0 Z" fill="var(--brand-blue)"/>
    </svg>
    <span class="brand-dot"></span>
    <span class="brand-name">KT4 Linkway</span>
    <div class="front-info">
      <h1 class="person-name">Name Of Person</h1>
      <p class="person-title">Title Of Person</p>
      <div class="rule"></div>
      <p class="contact-line">
        <svg viewBox="0 0 24 24"><path d="M6.6 10.8a15 15 0 0 0 6.6 6.6l2.2-2.2c.3-.3.7-.4 1-.2 1.1.4 2.3.6 3.6.6.6 0 1 .4 1 1V20c0 .6-.4 1-1 1A17 17 0 0 1 3 4c0-.6.4-1 1-1h3.5c.6 0 1 .4 1 1 0 1.3.2 2.5.6 3.6.1.3 0 .7-.2 1z"/></svg>
        +123 456 7890
      </p>
      <p class="contact-line">
        <svg viewBox="0 0 24 24"><path d="M2 5h20v14H2z M2 5l10 8 10-8" fill="none" stroke="#444" stroke-width="2"/></svg>
        name@email.com
      </p>
      <div class="rule"></div>
      <p class="front-web">www.website.com</p>
    </div>
  </section>

</main>
</body>
</html>
```